Computer repair shop

A card with our logo. And number and email and address. Our colors are baby /light blue and gray

Prefferably one sode with full logo - interested in other designs and options

Computer / laptop repair shop
On site support
Snall business IT support

```html
<!DOCTYPE html>
<html lang="en">
<head>
<meta charset="utf-8">
<title>Byte Fixers – Business Card</title>
<link rel="stylesheet" href="https://fonts.googleapis.com/css2?family=Lato:wght@400;700;900&family=Questrial&display=swap">
<style>
  :root {
    --page-bg: #e6e8eb;
    --card-bg: #ffffff;
    --brand-blue: #2a9fd8;
    --ink: #1c1c1c;
    --accent-red: #e3262b;
    --band-dark: #0d0d0d;
    --rule: #222222;
  }
  * { box-sizing: border-box; margin: 0; padding: 0; }
  html, body {
    width: 1200px; height: 1200px; overflow: hidden;
    background: var(--page-bg);
    font-family: "Lato", Arial, sans-serif;
    color: var(--ink);
  }
  .card {
    position: absolute; left: 210px; width: 768px; height: 440px;
    background: var(--card-bg);
    box-shadow: 0 6px 18px rgba(0,0,0,0.18);
    overflow: hidden;
  }
  .card--front { top: 134px; }
  .card--back { top: 622px; }
  .card__band { position: absolute; left: 0; right: 0; bottom: 0; height: 14px; }
  .card--front .card__band { background: var(--brand-blue); }
  .card--back .card__band { background: var(--band-dark); }

  .brand {
    position: absolute; left: 66px; top: 114px; width: 312px; height: 220px;
    display: flex; align-items: center; justify-content: center; gap: 12px;
  }
  .brand__dot { width: 22px; height: 22px; border-radius: 50%; background: var(--brand-blue); }
  .brand__name {
    font-family: "Lato", Arial, sans-serif; font-weight: 900;
    font-size: 44px; color: var(--brand-blue); letter-spacing: 0.5px;
  }

  .divider { position: absolute; width: 2px; background: var(--rule); }
  .card--front .divider { left: 430px; top: 115px; height: 217px; }
  .card--back .divider { left: 424px; top: 176px; height: 152px; }

  .contact { position: absolute; left: 458px; top: 114px; }
  .contact__name {
    font-family: "Questrial", Arial, sans-serif; font-weight: 400;
    font-size: 31px; color: var(--brand-blue); line-height: 1; letter-spacing: 0.5px;
    -webkit-text-stroke: 0.6px var(--brand-blue);
  }
  .contact__title { font-size: 18px; margin-top: 0; }
  .contact__city { font-size: 18px; margin-top: 20px; }
  .contact__list { list-style: none; margin-top: 21px; }
  .contact__item {
    display: flex; align-items: center; gap: 10px;
    font-size: 18px; height: 27px;
  }
  .contact__item svg { width: 16px; height: 16px; flex: none; fill: var(--accent-red); }

  .services { position: absolute; left: 454px; top: 176px; list-style: none; }
  .services__item {
    display: flex; align-items: center; gap: 16px;
    font-size: 18.5px; height: 49px; line-height: 1;
  }
  .services__item::before {
    content: ""; width: 8px; height: 8px; border-radius: 50%; background: var(--accent-red);
  }
</style>
</head>
<body>

<section class="card card--front">
  <div class="brand">
    <span class="brand__dot"></span>
    <span class="brand__name">Byte Fixers</span>
  </div>
  <div class="divider"></div>
  <div class="contact">
    <h1 class="contact__name">ALEX CARTER</h1>
    <p class="contact__title">Founder &amp; CEO</p>
    <p class="contact__city">London, UK</p>
    <ul class="contact__list">
      <li class="contact__item">
        <svg viewBox="0 0 24 24" aria-hidden="true"><path d="M6.6 10.8a15.1 15.1 0 0 0 6.6 6.6l2.2-2.2a1 1 0 0 1 1-.25 11.4 11.4 0 0 0 3.6.57 1 1 0 0 1 1 1V20a1 1 0 0 1-1 1A17 17 0 0 1 3 4a1 1 0 0 1 1-1h3.5a1 1 0 0 1 1 1c0 1.25.2 2.45.57 3.57a1 1 0 0 1-.25 1z"/></svg>
        000 000 0000
      </li>
      <li class="contact__item">
        <svg viewBox="0 0 24 24" aria-hidden="true"><path d="M6 2h12v5H6z"/><path d="M3 8h18a1 1 0 0 1 1 1v7h-4v-3H6v3H2V9a1 1 0 0 1 1-1z"/><path d="M7 14h10v8H7z"/></svg>
        999.999.9999
      </li>
      <li class="contact__item">
        <svg viewBox="0 0 24 24" aria-hidden="true"><path d="M2 5h20v2l-10 6L2 7z"/><path d="M2 9.3l10 6 10-6V19H2z"/></svg>
        a_carter@bytefixers.com
      </li>
      <li class="contact__item">
        <svg viewBox="0 0 24 24" aria-hidden="true"><path d="M12 2a10 10 0 1 0 0 20 10 10 0 0 0 0-20zm0 2c.9 0 2.2 1.7 2.8 5H9.2C9.8 5.7 11.1 4 12 4zM4.3 11h3.3v2H4.3a8 8 0 0 1 0-2zm.6 4h2.9c.3 1.6.8 3 1.4 4a8 8 0 0 1-4.3-4zm2.9-6H4.9a8 8 0 0 1 4.3-4c-.6 1-1.1 2.4-1.4 4zM12 20c-.9 0-2.2-1.7-2.8-5h5.6c-.6 3.3-1.9 5-2.8 5zm-3-7v-2h6v2zm5.8 6c.6-1 1.1-2.4 1.4-4h2.9a8 8 0 0 1-4.3 4zm1.6-6v-2h3.3a8 8 0 0 1 0 2zm-.2-4c-.3-1.6-.8-3-1.4-4a8 8 0 0 1 4.3 4z"/></svg>
        www.bytefixers.com
      </li>
    </ul>
  </div>
  <div class="card__band"></div>
</section>

<section class="card card--back">
  <div class="brand">
    <span class="brand__dot"></span>
    <span class="brand__name">Byte Fixers</span>
  </div>
  <div class="divider"></div>
  <ul class="services">
    <li class="services__item">Computer / laptop repair shop</li>
    <li class="services__item">On site support</li>
    <li class="services__item">Snall business IT support</li>
  </ul>
  <div class="card__band"></div>
</section>

</body>
</html>
```